5 Email Newsletter Templates Needed

We need 5 email templates for our email marketing campaign. We are an Insurance Agency in Los Angeles called KDP-Silverbrook Insurance Services. We use Mailvane Hub as our email marketing platform. The templates need to be simple, a nice header, not to busy and you will need to use our color palette. The first email template we need is for our current clients / prospects. The content we will put in this email will be insurance tips and information, short and simple about 2 small paragraphs. The next 3 templates all need to be the same but different colors. One red, one yellow and one green. These will be alerts from kdp-silverbrook. An example a major earthquake hits we will send a red alert. A legislative change on healthcare and we send a yellow alert. We buy another location and we send a green alert. The last email is for our COINs (Centers of Influence, the people who refer business to us). I uploaded an email from one of our business consultants to give an idea of the size and sophistication we are looking for. I also uploaded our corporate brochure and color palette so you can learn more about our firm.

Target Market(s)

Our target markets are commercial business 1mm plus in revenue, 500 employees, high net worth individuals. Our COINs are CPAs, CFOs, Business Managers

Requirements
Nice to have
• HTML Code is desired. You can also provide just an image file for the header and our email marketing program will do the coding for us.
Should not have
• No cartoon looking graphics. Do not use old-style fonts like Times New Roman.

```html
<!DOCTYPE html>
<html lang="en">
<head>
<meta charset="utf-8">
<title>KDP-Silverbrook Insurance Services – Healthcare Alert</title>
<link href="https://fonts.googleapis.com/css2?family=Arimo:wght@400;700&display=swap" rel="stylesheet">
<style>
  :root {
    --page-yellow: #f7d900;
    --card-white: #ffffff;
    --ink: #1e1e1e;
    --heading-orange: #f26a0f;
    --brand-navy: #1d4a7a;
    --bar-teal: #0f7a63;
    --bar-orange: #c9540e;
    --bar-maroon: #7a3040;
    --bar-purple: #574a78;
    --banner-yellow: #f4c400;
    --link-purple: #3e3470;
    --photo-gray: #c9c9c9;
    --social-blue: #4a7fc0;
    --badge-gray: #e3e6ea;
  }
  * { box-sizing: border-box; margin: 0; padding: 0; }
  html, body { width: 1200px; height: 987px; overflow: hidden; }
  body {
    background: var(--page-yellow);
    font-family: "Arimo", Arial, sans-serif;
    color: var(--ink);
    position: relative;
  }
  .card {
    position: absolute;
    left: 243px; top: 30px;
    width: 715px; height: 836px;
    background: var(--card-white);
  }
  .card__sheen {
    position: absolute; left: 0; top: 0; width: 100%; height: 24px;
    background: linear-gradient(#f6f1dc, #ffffff);
  }
  .card__fold { position: absolute; right: 0; top: 0; }
  .card__shadow {
    position: absolute; left: 260px; top: 866px; width: 680px; height: 30px;
    background: radial-gradient(ellipse at 50% 0%, rgba(0,0,0,.55), rgba(0,0,0,0) 70%);
  }
  .masthead {
    position: absolute; left: 18px; top: 32px; width: 680px; height: 62px;
  }
  .brand {
    position: absolute; left: 0; top: 20px;
    font-size: 22px; font-weight: 400; color: var(--ink);
  }
  .social {
    position: absolute; right: 0; top: 14px;
    display: flex; align-items: center; gap: 4px;
    font-size: 17px;
  }
  .social__label { margin-right: 6px; }
  .social__square { width: 32px; height: 32px; border-radius: 5px; background: var(--social-blue); }
  .social__square--light { background: #6fb8e0; }
  .banner {
    position: absolute; left: 18px; top: 107px; width: 680px; height: 119px;
    display: flex;
  }
  .banner__panel {
    width: 341px; height: 100%;
    background: radial-gradient(circle, rgba(0,0,0,.12) 1px, transparent 1.3px) 0 0/4px 4px, var(--banner-yellow);
    display: flex; align-items: center; padding-left: 23px;
  }
  .banner__title { font-size: 34px; font-weight: 400; color: #111; text-shadow: 1px 1px 0 rgba(255,255,255,.5); }
  .banner__photo {
    flex: 1;
    background: linear-gradient(100deg, #d8dde2, #f1f3f5 45%, #9bb3d6 60%, #e6e9ec);
  }
  .stripe { display: flex; gap: 2px; height: 5px; width: 680px; }
  .stripe span { flex: 1; }
  .stripe .s1 { background: var(--bar-teal); }
  .stripe .s2 { background: var(--bar-orange); }
  .stripe .s3 { background: var(--bar-maroon); }
  .stripe .s4 { background: var(--bar-purple); }
  .stripe--banner { position: absolute; left: 18px; top: 227px; }
  .stripe--divider { position: absolute; left: 18px; top: 683px; }
  .article {
    position: absolute; left: 18px; top: 263px; width: 688px;
    font-size: 14.6px; line-height: 21.5px;
  }
  .article__lead { font-size: 21px; font-weight: 700; color: var(--heading-orange); margin-bottom: 22px; }
  .article__figure {
    float: left; width: 169px; height: 113px; margin: 4px 14px 6px 0;
    border: 5px solid var(--photo-gray);
    background: linear-gradient(135deg, #eef1f5, #b9c6d6 55%, #8e9bab);
  }
  .article__sub { clear: both; font-size: 16.5px; font-weight: 700; color: var(--heading-orange); margin: 16px 0 8px; }
  .tips { list-style: none; margin: 14px 0 0 40px; }
  .tips li { position: relative; padding-left: 16px; margin-bottom: 3px; }
  .tips li::before {
    content: ""; position: absolute; left: 1px; top: 8px; width: 6px; height: 6px;
    background: var(--brand-navy); transform: rotate(45deg);
  }
  .signoff {
    position: absolute; left: 18px; top: 705px; width: 672px;
    font-size: 14.6px; line-height: 21.5px;
  }
  .contact { position: absolute; left: 18px; top: 770px; }
  .contact__visit { font-size: 16.7px; }
  .contact__visit a { color: var(--link-purple); text-decoration: none; }
  .contact__address { font-size: 14.2px; margin-top: 3px; }
  .badge {
    position: absolute; left: 632px; top: 746px; width: 64px; height: 64px;
    background: var(--badge-gray);
  }
  .card__base { position: absolute; left: 0; bottom: 0; width: 100%; height: 6px; background: var(--bar-purple); }
  .footer {
    position: absolute; left: 0; top: 916px; width: 1200px; text-align: center;
    font-size: 12px; line-height: 21px; color: #000;
  }
  .footer__sent { color: #4a3a00; }
  .footer__sent b { font-weight: 400; color: #000; }
  .footer__links a { color: #000; font-weight: 700; text-decoration: underline; }
  .footer__links span.plain { font-weight: 400; }
</style>
</head>
<body>
  <div class="card__shadow"></div>
  <main class="card">
    <div class="card__sheen"></div>
    <svg class="card__fold" width="36" height="44" viewBox="0 0 36 44" aria-hidden="true">
      <polygon points="0,0 36,44 36,0" fill="#f7d900"/>
      <polygon points="0,0 36,44 14,30" fill="#d8d8d8"/>
    </svg>

    <header class="masthead">
      <div class="brand">KDP-Silverbrook Insurance Services</div>
      <div class="social">
        <span class="social__label">Stay in Touch</span>
        <span class="social__square social__square--light"></span>
        <span class="social__square"></span>
      </div>
    </header>

    <section class="banner">
      <div class="banner__panel"><h1 class="banner__title">Healthcare...</h1></div>
      <div class="banner__photo" role="img" aria-label="Photo of a technician preparing a patient for a medical scan"></div>
    </section>
    <div class="stripe stripe--banner"><span class="s1"></span><span class="s2"></span><span class="s3"></span><span class="s4"></span></div>

    <article class="article">
      <h2 class="article__lead">Lorem Ipsum is simply dummy text of the printing.</h2>
      <div class="article__figure" role="img" aria-label="Photo of a stethoscope and pen on a medical chart"></div>
      <p>Lorem Ipsum is simply dummy text of the printing and typesetting industry. Lorem Ipsum has been the industry's standard dummy text ever since the 1500s, when an unknown printer took a galley of type and scrambled it to make a type specimen book. It has survived not only five centuries, but also the leap into electronic typesetting, remaining essentially unchanged. It was popularised in the 1960s with the release of Lettrine sheets containing Lorem Ipsum passages, and more recently with desktop publishing software like Folio Layout including versions of Lorem Ipsum.</p>
      <h3 class="article__sub">Lorem Ipsum is simply dummy text of the printing.</h3>
      <p>The standard chunk of Lorem Ipsum used since the 1500s is reproduced below for those interested.<br>Sections 1.10.32 and 1.10.33 from "de Finibus Bonorum et Malorum" by Cassius Varro are also reproduced in their exact original form, accompanied by English versions from the 1914 translation by H. Ralston.</p>
      <ul class="tips">
        <li>Lorem ipsum dolor sit amet, consectetur adipiscing elit.</li>
        <li>Curabitur convallis accumsan dolor, a venenatis massa fermentum sed.</li>
      </ul>
    </article>

    <div class="stripe stripe--divider"><span class="s1"></span><span class="s2"></span><span class="s3"></span><span class="s4"></span></div>

    <p class="signoff">Be on the lookout for next week's tip from KDP-Silverbrook. If you have additional questions or would like to talk with a professional about your business continuity needs...</p>

    <div class="contact">
      <p class="contact__visit">Please visit <a href="#">www.kdp-silverbrook.com</a> or Call at <b>(555) 201-7740</b></p>
      <p class="contact__address"><b>Silverbrook Insurance Services, Inc.</b> 2280 Laurel Vista Ave., Ste 310, Larkfield, CA 90000</p>
    </div>
    <div class="badge" role="img" aria-label="Partner badge"></div>

    <div class="card__base"></div>
  </main>

  <footer class="footer">
    <p class="footer__sent">This message was sent to <b>jordan.lee@clientmail.com</b> by <b>hello@sendmail.com</b></p>
    <p class="footer__links"><a href="#">Unsubscribe</a> | <a href="#">Update</a> | <a href="#">Forward Email</a> | <span class="plain">Report Abuse</span></p>
  </footer>
</body>
</html>
```